Redesign of a facility management homepage

We need a redesign/an improved design of the facility management homepage (http://www.krt-lanzfeld.de/).
This websites offers detailed information on the "About us" as company, the "Services" provided and special information on facility and strata management. We would like to keep the structure of the website.
We need ideas/designs how this website could look more modern and confidential and appealing/pleasant for visitors at the same time and not losing the main purpose of information distribution.
The green color must be used since this is the basic color from our logo.
The blue in the background of the logo ist optional. So feel to use it or not.
We need no coding only design (.psd or as .ai)

```html
<!DOCTYPE html>
<html lang="en">
<head>
<meta charset="utf-8">
<title>KRT Lanzfeld – Office and Janitorial Service</title>
<link href="https://fonts.googleapis.com/css2?family=Mulish:wght@400;500;600;700&family=Nunito:wght@500;600&display=swap" rel="stylesheet">
<style>
:root{
  --green:#2e8b37;
  --green-dark:#1f6f29;
  --green-text:#2a8a2f;
  --text:#444;
  --muted:#666;
  --footer:#4a4a4a;
  --frame:#d4d4d4;
  --white:#fff;
}
*{margin:0;padding:0;box-sizing:border-box}
html,body{width:1008px;height:1200px;overflow:hidden;background:var(--white)}
body{position:relative;font-family:"Mulish",sans-serif;color:var(--text)}
.abs{position:absolute}
a{color:inherit;text-decoration:none}

.topbar{left:0;top:0;width:1008px;height:34px;background:var(--green);color:var(--white);font-size:10.5px}
.topbar .util{left:62px;top:10px}
.topbar .util span{margin:0 4px}
.topbar .contact{right:61px;top:9px;font-size:12px;font-weight:600;display:flex;align-items:center;gap:6px}

.brand-mark{left:63px;top:41px;width:106px;height:85px;background:linear-gradient(135deg,#b6cdea,#7ea2d4);display:flex;align-items:center;justify-content:center;font-size:26px;font-weight:700;color:var(--white)}
.brand-name{left:198px;top:53px;color:var(--green-text);font-size:20.5px;line-height:21px;font-weight:500}
.brand-tag{left:198px;top:98px;color:var(--green-text);font-size:14.5px;font-weight:500}

.nav{left:494px;top:98px;display:flex;align-items:center;font-size:12px;color:#555;letter-spacing:.2px}
.nav a{padding:0 11px;height:29px;line-height:29px}
.nav a.active{background:var(--green);color:var(--white);padding:0 13px}
.nav a:nth-child(3){padding-right:14px}

.slider{left:63px;top:134px;width:883px;height:362px;border:4px solid var(--frame);
  background:
    radial-gradient(ellipse 120px 90px at 260px 250px,rgba(40,40,40,.55),transparent 70%),
    radial-gradient(ellipse 160px 110px at 520px 240px,rgba(200,40,40,.55),transparent 70%),
    radial-gradient(ellipse 150px 110px at 760px 230px,rgba(210,45,45,.5),transparent 70%),
    linear-gradient(180deg,#2f4a22 0%,#3f5e2c 35%,#5a4a3a 55%,#8c8a84 75%,#c8c6c0 100%)}
.caption{left:0;top:150px;width:418px;height:54px;background:rgba(40,40,40,.72);color:var(--white);font-family:"Nunito",sans-serif;font-size:28px;line-height:54px;padding-left:32px;letter-spacing:.3px}
.dots{left:416px;top:334px;display:flex;gap:5px}
.dots i{width:9px;height:9px;border-radius:50%;background:#555;display:block}
.dots i:first-child{background:var(--green)}

.welcome h1{left:63px;top:518px;font-size:23px;font-weight:500;color:var(--green-text)}
.welcome .copy{left:65px;top:556px;width:585px;font-size:10.2px;line-height:18.5px;color:var(--text)}
.welcome .copy p{margin-bottom:3px}
.van{left:668px;top:540px;width:278px;height:152px;
  background:radial-gradient(ellipse 130px 60px at 140px 75px,#eef0f2 0%,#d6d9dc 70%,rgba(255,255,255,0) 100%)}

.rule{left:63px;top:711px;width:883px;border-top:2px dotted #ccc}

.card{top:748px;width:175px;height:206px;border:1px solid #ddd}
.card .photo{position:absolute;left:0;top:0;width:100%;height:168px}
.card .label{position:absolute;left:0;bottom:0;width:100%;height:37px;background:var(--green);color:var(--white);font-family:"Nunito",sans-serif;font-size:14px;font-weight:600;text-align:center;line-height:44px}
.card .badge{position:absolute;left:50%;top:140px;width:34px;height:34px;margin-left:-17px;border-radius:50%;background:var(--green);display:flex;align-items:center;justify-content:center}

.news h2,.quick h2{font-size:19px;font-weight:500;color:var(--green-text)}
.news h2{left:63px;top:977px}
.news-dots{left:513px;top:988px;display:flex;gap:3px}
.news-dots i{width:9px;height:9px;border-radius:50%;border:1px solid #555;display:block}
.news-dots i:first-child{background:var(--green);border-color:var(--green-dark)}
.item{top:1009px;width:290px;height:67px}
.item .thumb{position:absolute;left:0;top:0;width:91px;height:67px}
.item h3{position:absolute;left:101px;top:3px;font-size:11px;font-weight:600;color:var(--green-text)}
.item p{position:absolute;left:101px;top:20px;width:185px;font-size:10px;line-height:14.5px;color:#333}

.quick h2{left:691px;top:977px}
.quick p{left:693px;top:1010px;width:260px;font-size:10px;line-height:15.5px;color:var(--muted)}
.quick .btn{left:693px;top:1042px;width:97px;height:35px;border-radius:3px;background:linear-gradient(180deg,#3a9b3f,#1c6c23);color:var(--white);font-size:11px;font-weight:600;text-align:center;line-height:35px}

.footer{left:0;top:1106px;width:1008px;height:94px;background:var(--footer);color:var(--white)}
.footer .links{left:63px;top:18px;font-size:9px;display:flex;gap:18px;letter-spacing:.2px}
.footer .copy{left:63px;top:60px;font-size:9.5px}
.footer .connect{left:810px;top:40px;font-size:12px;font-weight:500}
.social{top:35px;width:25px;height:25px;background:#6b7a99}
</style>
</head>
<body>

<header>
  <div class="abs topbar">
    <div class="abs util"><a>Support</a><span>|</span><a>Links</a><span>|</span><a>Imprint</a><span>|</span><a>Contact Us</a></div>
    <div class="abs contact">
      <svg width="12" height="12" viewBox="0 0 12 12"><rect width="12" height="12" rx="2" fill="#fff"/><path d="M3.5 2.5l1.5 0 .6 2-1 .8a5 5 0 0 0 2.1 2.1l.8-1 2 .6v1.5c0 .5-.5 1-1 1A6.5 6.5 0 0 1 2.5 3.5c0-.5.5-1 1-1z" fill="#2e8b37"/></svg>
      <span>Tel: 0 34 12/58 27 14</span><span>&nbsp;|&nbsp;</span>
      <svg width="15" height="10" viewBox="0 0 15 10"><rect width="15" height="10" fill="#fff"/><path d="M0 0l7.5 6L15 0" stroke="#2e8b37" fill="none"/></svg>
      <span>Email: info@krt-lanzfeld.de</span>
    </div>
  </div>

  <div class="abs brand-mark">KRT</div>
  <div class="abs brand-name">Office and Janitorial Service<br>GmbH Lanzfeld</div>
  <div class="abs brand-tag">Your local partner.</div>

  <nav class="abs nav">
    <a class="active">HOME</a><a>ABOUT US</a><a>BUILDING MANAGEMENT</a><a>RENTAL</a><a>CONTACT US</a>
  </nav>
</header>

<section class="abs slider" role="img" aria-label="Red ride-on mower and snow blowers with plough blades on paving in front of green shrubs">
  <div class="abs caption">Cleaning Sweeping Services</div>
  <div class="abs dots"><i></i><i></i><i></i><i></i></div>
</section>

<section class="welcome">
  <h1 class="abs">Welcome to Our Website !!</h1>
  <div class="abs copy">
    <p>The KRT is an established, experienced and successful services company with the divisions Buildings Management (facilities management, operating expense reports, etc.), concierge service, winter maintenance, building services, secretarial services, etc.</p>
    <p>The KRT has the latest computer programs and trained, highly experienced and motivated staff.</p>
    <p>The KRT guarantees comprehensive support, thereby ensuring preservation of value of the contract objects. Furthermore, the standing KRT also for the optimization of the net results of the individual property investments in terms of costs and revenues. Most of the KRT managed objects have extremely low vacancy rates.</p>
  </div>
  <div class="abs van" role="img" aria-label="White company service van with roof rack"></div>
</section>

<div class="abs rule"></div>

<section class="cards">
  <div class="abs card" style="left:63px">
    <div class="photo" role="img" aria-label="Smiling customer service agent with headset" style="background:radial-gradient(ellipse 70px 80px at 120px 70px,#e8c7ae,transparent 75%),linear-gradient(135deg,#d9c2b2,#f1ece8 60%,#b98a6c)"></div>
    <div class="badge"><svg width="18" height="18" viewBox="0 0 18 18" fill="none" stroke="#fff" stroke-width="1.8"><path d="M3 10V8a6 6 0 0 1 12 0v2"/><rect x="2" y="9" width="3" height="5" rx="1" fill="#fff"/><rect x="13" y="9" width="3" height="5" rx="1" fill="#fff"/><path d="M14 14c0 2-2 2.5-4 2.5"/></svg></div>
    <div class="label">Report disorder online</div>
  </div>
  <div class="abs card" style="left:297px">
    <div class="photo" role="img" aria-label="Hand holding a handwritten contact note" style="background:radial-gradient(ellipse 55px 45px at 88px 75px,#efe4b8,transparent 80%),linear-gradient(135deg,#f4f1ec,#e6c3a0)"></div>
    <div class="badge"><svg width="18" height="16" viewBox="0 0 18 16" fill="#fff"><path d="M1 6c0-3 16-3 16 0v2h-4V6.5H5V8H1z"/><path d="M4 9h10l2 6H2z"/><circle cx="9" cy="12" r="1.8" fill="#2e8b37"/></svg></div>
    <div class="label">Contact</div>
  </div>
  <div class="abs card" style="left:535px">
    <div class="photo" role="img" aria-label="Hands typing on a dark keyboard" style="background:radial-gradient(ellipse 70px 45px at 115px 40px,#d6a888,transparent 80%),linear-gradient(170deg,#b89a88 0%,#5a5a5e 45%,#2a2a2c 100%)"></div>
    <div class="badge"><svg width="14" height="17" viewBox="0 0 14 17" fill="none" stroke="#fff" stroke-width="1.5"><path d="M1 1h8l4 4v11H1z"/><path d="M4 8h6M4 11h6M4 14h4"/></svg></div>
    <div class="label">Left</div>
  </div>
  <div class="abs card" style="left:772px">
    <div class="photo" role="img" aria-label="Hands sheltering a small model house with red roof" style="background:radial-gradient(ellipse 45px 30px at 88px 115px,#c9503e,transparent 80%),linear-gradient(180deg,#eadad0,#f3ede8 55%,#bfa58f)"></div>
    <div class="badge"><svg width="18" height="16" viewBox="0 0 18 16" fill="#fff"><path d="M9 1L1 8h2.5v7h4v-4h3v4h4V8H17z"/></svg></div>
    <div class="label">Imprint</div>
  </div>
</section>

<section class="news">
  <h2 class="abs">Latest News</h2>
  <div class="abs news-dots"><i></i><i></i><i></i></div>
  <article class="abs item" style="left:63px">
    <div class="thumb" role="img" aria-label="Blue compact utility vehicle" style="background:linear-gradient(180deg,#c9c2b4,#3a5d9a 55%,#6c6a66)"></div>
    <h3>Lorem ipsum dolor sit amet</h3>
    <p>Lorem ipsum dolor sit amet, consetetur sadipscing elitr, sed diam nonumy eirmod tempor</p>
  </article>
  <article class="abs item" style="left:361px">
    <div class="thumb" role="img" aria-label="Rear of the white service van" style="background:linear-gradient(135deg,#5a5a5a,#f2f2f2 45%,#c4c6c8)"></div>
    <h3>Lorem ipsum dolor sit amet</h3>
    <p>Lorem ipsum dolor sit amet, consetetur sadipscing elitr, sed diam nonumy eirmod tempor</p>
  </article>
</section>

<section class="quick">
  <h2 class="abs">Quick Contact</h2>
  <p class="abs">Nunc tempus felis vitae urna Vivamus porttitor g purus nisi eleifend libero a tempus libero lectus</p>
  <a class="abs btn">CLICK HERE</a>
</section>

<footer class="abs footer">
  <div class="abs links"><a>HOME</a><a>ABOUT US</a><a>BUILDING MANAGEMENT</a><a>RENTAL</a><a>CONTACT US</a></div>
  <div class="abs copy">Copyright © 2014. KRT. All Right Reserved</div>
  <div class="abs connect">Connect Us:</div>
  <div class="abs social" style="left:889px" aria-label="Social profile one"></div>
  <div class="abs social" style="left:922px" aria-label="Social profile two"></div>
</footer>

</body>
</html>
```